Website Design for Chef Varo Chinese Restaurant

Chef Varo is a new Chinese Restaurant. It offers exceptional dining experience with authentic and dynamic dishes created with quality ingredients.

A vivid website theme is required to promote this new restaurant online. Logo, menu, wine list and a few other files are attached for help with designing.

A very rough demo website has been setup and can be accessed via http://www.chefvaro.com.au. It is for telling designers what content is shown up on each page (except for homepage). By reading the about us page, designers can get some more info of Chef Varo. However, the layout, theme color, font, etc are not set in stone. Visitors should be able to feel Chef Varo restaurant's authentic Chinese cuisine and high hygiene standard. Home page of the website could be The "Our website is coming soon" description is shown on demo site but do not required to be presented on new design.

Some main pages design should be included: Home (landing page), About us, Menu (Dishes), Winelist, Gallery, Contact us. No HTML and coding required. The output should be well layered psd or png files with acceptable resolution for web use.

A few other website can be referred to are:

http://belmiraeatery.com.au/
http://www.stone-kettle.com/
http://quillhaven.com.au/
http://meadowbistro.com.au/
http://www.lanternvaledining.com.au/
http://www.thetrove.com.au/

Industry/Entity Type

Restaurant

Requirements
Nice to have
• I expect designs of at least these webpages: homepage, menu page and contact us page. If you can provide "about us" page as well, it will probably help you win the competition. well layered psd or png file is my preference.
Should not have
• You don't have to make html/cs/js or any coding. All I need is just art design

```html
<!DOCTYPE html>
<html lang="en">
<head>
<meta charset="utf-8">
<title>Chef Varo Chinese Restaurant</title>
<link href="https://fonts.googleapis.com/css2?family=Arimo:wght@400;700&display=swap" rel="stylesheet">
<style>
:root{
  --red:#dd0000;
  --red-dark:#b80000;
  --cream:#fffbd0;
  --beige:#e9e2b2;
  --panel:#e6e6e6;
  --ink:#222;
  --dark:#262626;
  --white:#fff;
}
*{box-sizing:border-box;margin:0;padding:0}
html,body{width:891px;height:1200px;overflow:hidden}
body{position:relative;background:var(--white);font-family:"Arimo",Arial,sans-serif;color:var(--ink)}
.abs{position:absolute}
.header{left:0;top:0;width:891px;height:132px;background:var(--cream)}
.brand{left:0;top:40px;width:891px;text-align:center;color:var(--red);font-weight:700}
.brand-mark{display:inline-block;width:16px;height:16px;background:var(--red);vertical-align:middle;margin-right:8px}
.brand-name{font-size:17px;vertical-align:middle;letter-spacing:.5px}
.hero{left:0;top:132px;width:891px;height:270px;background:linear-gradient(180deg,#dccd96 0%,#efe6bf 45%,#f8f2d6 100%)}
.hero-photo{left:105px;top:24px;width:640px;height:230px;border-radius:120px;background:radial-gradient(ellipse at center,#c96a3a 0%,#d9a868 45%,rgba(224,196,140,0) 75%)}
.hero-deco{top:130px;width:190px;height:120px;border-radius:60px;background:rgba(120,95,50,.15)}
.arrow{width:37px;height:37px;border-radius:50%;background:#3a3a3a;border:2px solid #888;top:122px}
.dots{left:418px;top:254px;display:flex;gap:8px}
.dots span{width:8px;height:8px;border-radius:50%;background:#333}
.dots span:first-child{background:var(--red)}
.nav{left:65px;top:124px;width:761px;height:30px;background:var(--red);display:flex;align-items:center;justify-content:space-between;padding:0 20px;box-shadow:0 2px 2px rgba(0,0,0,.25)}
.nav a{color:var(--white);font-weight:700;font-size:16px;text-decoration:none}
.nav a.current{color:#3a0000}
.stars{color:#ffe94a;font-size:11px;letter-spacing:3px}
.divider{left:386px;top:404px;width:120px;height:34px;border-radius:50%;background:rgba(221,0,0,.25)}
.panel{background:var(--panel);border:1px solid #fff;outline:1px solid #ddd}
.tab{background:var(--red);color:var(--white);font-size:21px;display:flex;align-items:center;justify-content:center;gap:8px;box-shadow:0 1px 2px rgba(0,0,0,.3)}
.wine{left:58px;top:461px;width:776px;height:181px}
.wine-photo{left:0;top:0;width:226px;height:181px;background:linear-gradient(90deg,#9c1c2a 0%,#e8e8e8 55%,#d8cfa6 100%)}
.wine-col h3{color:var(--red);font-weight:400;font-size:15px;margin-bottom:6px}
.wine-col li{list-style:none;font-size:12.5px;line-height:23px;padding-left:12px;position:relative}
.wine-col li::before{content:"";position:absolute;left:0;top:8px;width:6px;height:8px;background:var(--red);border-radius:50% 50% 50% 50%/60% 60% 40% 40%}
.wine-col.red li{line-height:21px}
.welcome{left:58px;top:662px;width:776px;height:226px}
.welcome-text{left:22px;top:42px;width:480px;font-size:10.4px;line-height:17px}
.welcome-text p+p{margin-top:16px}
.welcome-photo{left:520px;top:2px;width:252px;height:220px;border-radius:90px;background:radial-gradient(ellipse at center,#b8693a 0%,#d9b070 50%,rgba(230,230,230,0) 78%)}
.btn{background:var(--red);color:var(--white);font-weight:700;font-size:12px;border:2px solid #fff;outline:1px solid var(--red);display:flex;align-items:center;justify-content:center}
.box{background:var(--red);border:1px solid #fff;outline:1px solid var(--red-dark);color:var(--white)}
.box-tab{background:var(--beige);color:var(--red);font-size:21px;display:flex;align-items:center;justify-content:center;gap:8px}
.hours{left:58px;top:914px;width:381px;height:192px;padding:42px 0 0 17px}
.hours .lead{font-size:17px;margin-bottom:16px}
.hours p{font-size:13px;line-height:17.5px}
.hours p.gap{margin-top:16px}
.news{left:455px;top:914px;width:381px;height:192px}
.field-label{font-size:12px;font-weight:700;color:var(--white)}
.field{width:232px;height:27px;background:var(--cream);border:1px solid #f0e8a0}
.submit{background:var(--beige);color:var(--red);font-weight:700;font-size:11.5px;display:flex;align-items:center;justify-content:center;border:2px solid #c9c08a}
.footer{left:0;top:1128px;width:891px;height:72px;background:var(--dark);border-top:4px solid var(--red)}
.footer-nav{left:160px;top:13px;display:flex;gap:0}
.footer-nav a{color:#eee;font-size:12.5px;text-decoration:none;margin-right:0}
.copy{left:0;top:44px;width:891px;text-align:center;color:#ddd;font-size:10.5px}
.copy strong{color:var(--red);font-weight:400}
</style>
</head>
<body>
<header class="abs header">
  <div class="abs brand"><span class="brand-mark"></span><span class="brand-name">CHEF VARO CHINESE RESTAURANT</span></div>
</header>

<section class="abs hero">
  <div class="abs hero-deco" style="left:40px" role="img" aria-label="Decorative gold scroll ornament"></div>
  <div class="abs hero-deco" style="left:661px" role="img" aria-label="Decorative gold scroll ornament"></div>
  <div class="abs hero-photo" role="img" aria-label="Dim sum dishes in bamboo steamers: custard buns, chicken feet and spare ribs"></div>
  <div class="abs arrow" style="left:89px"><svg width="33" height="33" viewBox="0 0 33 33"><path d="M19 9 L12 16.5 L19 24" stroke="#fff" stroke-width="2" fill="none"/></svg></div>
  <div class="abs arrow" style="left:777px"><svg width="33" height="33" viewBox="0 0 33 33"><path d="M14 9 L21 16.5 L14 24" stroke="#fff" stroke-width="2" fill="none"/></svg></div>
  <div class="abs dots"><span></span><span></span><span></span><span></span></div>
</section>

<nav class="abs nav">
  <span class="stars">★★★</span>
  <a class="current" href="#">Home</a><a href="#">About</a><a href="#">Menu</a><a href="#">Winelist</a><a href="#">Facilities</a><a href="#">Gallery</a><a href="#">Contact</a>
  <span class="stars">★★★</span>
</nav>

<div class="abs divider" role="img" aria-label="Red decorative flourish"></div>

<section class="abs panel wine">
  <div class="abs wine-photo" role="img" aria-label="Glasses of red and white wine splashing"></div>
  <div class="abs wine-col" style="left:230px;top:38px"><h3>WINES</h3><ul><li>Champagne</li><li>Sparkling White</li><li>Sparkling Red</li></ul></div>
  <div class="abs wine-col" style="left:400px;top:38px"><h3>WHITE WINE</h3><ul><li>Riesling</li><li>Pinot Gris / Pinot Grigio</li><li>Sauvignon Blanc and Blends</li><li>Chardonnay</li><li>Other White Varietals</li></ul></div>
  <div class="abs wine-col red" style="left:590px;top:38px"><h3>RED WINE</h3><ul><li>Rosé</li><li>Pinot Noir</li><li>Grenache/Sangiovese/Merlot</li><li>Cabernet Sauvignon &amp; Blends</li><li>Shiraz and Blends</li><li>Other Red Varietals</li></ul></div>
</section>
<div class="abs tab" style="left:346px;top:452px;width:198px;height:30px">
  <svg width="20" height="20" viewBox="0 0 20 20"><path d="M3 17 L11 9 M10 4 l6 6 l-3 3 l-6 -6z" stroke="#fff" stroke-width="2.4" fill="#fff"/></svg>Winelist
</div>

<section class="abs panel welcome">
  <div class="abs welcome-text">
    <p>Chef Varo is named after its' executive chef, Mr. Varo. Chef Varo has been in his career for nearly two decades before he moved to Australia nine years ago. He settled in Adelaide then started his first restaurant, Belmira Court in Norwood. Belmira Court has been running successfully for years due to Chef Varo's talent of cooking.</p>
    <p>We offer an exceptional dining experience with authentic and dynamic dishes created with quality ingredients. The menu of Chef Varo is based on classic Cantonese dishes, featured by southern China's local flavour characteristics. Taking advantage of South Australia's rich and quality food resources...</p>
  </div>
  <div class="abs welcome-photo" role="img" aria-label="Steamed dumplings, meatballs and dim sum in bamboo baskets"></div>
  <div class="abs btn" style="left:416px;top:188px;width:102px;height:29px">READ MORE</div>
</section>
<div class="abs tab" style="left:295px;top:654px;width:301px;height:30px">
  <svg width="22" height="20" viewBox="0 0 22 20"><path d="M11 2 L1 11 H4 V19 H9 V13 H13 V19 H18 V11 H21z" fill="#fff"/></svg>Welcome to&nbsp; Chef Varo
</div>

<section class="abs box hours">
  <p class="lead">We are open 7 days</p>
  <p><b>Lunch</b> :</p>
  <p>Monday to Friday 11:30am – 2:30pm</p>
  <p>Saturday to Sunday 11:00am – 3:00pm</p>
  <p class="gap"><b>Dinner</b> :</p>
  <p>Monday to Sunday 6:00pm Until Late</p>
</section>
<div class="abs box-tab" style="left:100px;top:906px;width:300px;height:30px">
  <svg width="20" height="20" viewBox="0 0 20 20"><circle cx="10" cy="10" r="8" stroke="#dd0000" stroke-width="2" fill="none"/><path d="M10 5 V10 H6" stroke="#dd0000" stroke-width="2" fill="none"/></svg>Opening Hours
</div>

<section class="abs box news">
  <div class="abs field-label" style="left:69px;top:38px">Name</div>
  <div class="abs field" style="left:69px;top:55px"></div>
  <div class="abs field-label" style="left:69px;top:90px">Email</div>
  <div class="abs field" style="left:69px;top:107px"></div>
  <div class="abs submit" style="left:69px;top:148px;width:101px;height:30px">SUBMIT</div>
</section>
<div class="abs box-tab" style="left:497px;top:906px;width:300px;height:30px">
  <svg width="28" height="20" viewBox="0 0 28 20"><rect x="4" y="2" width="22" height="16" stroke="#dd0000" stroke-width="2" fill="none"/><path d="M4 6 H1 V18 H4 M8 6 H14 V11 H8z M17 6 H23 M17 10 H23 M8 14 H23" stroke="#dd0000" stroke-width="1.6" fill="none"/></svg>Newsletter
</div>

<footer class="abs footer">
  <div class="abs footer-nav">
    <a href="#" style="color:var(--red);width:75px">Home</a><a href="#" style="width:82px">About</a><a href="#" style="width:76px">Menu</a><a href="#" style="width:96px">Winelist</a><a href="#" style="width:101px">Facilities</a><a href="#" style="width:87px">Events</a><a href="#">Contact</a>
  </div>
  <div class="abs copy">© <strong>Chef Varo</strong> - 2014. All Rights Reserved.</div>
</footer>
</body>
</html>
```